Powerpoint Presentation

We have a basic 8 page presentation that we would like created on powerpoint. The presentation is very simple dot points and we would like to jazz it up with relevant photos/images relating to the topic on each page.

The topic of the presentation is 'creating a powerful presence and knowing your personal brand' (see attached files).

Target Market(s)

Business women

Requirements
Must have
• Images that match the content on each page

```html
<!DOCTYPE html>
<html lang="en">
<head>
<meta charset="utf-8">
<title>Networking</title>
<link href="https://fonts.googleapis.com/css2?family=Carlito:ital,wght@0,400;0,700;1,700&display=swap" rel="stylesheet">
<style>
  :root {
    --sky-deep: #1a8ad6;
    --sky-mid: #3aa6ea;
    --sky-light: #8fd0f6;
    --sky-pale: #d4eefc;
    --paper: #ffffff;
    --ink: #2b2b2b;
    --ink-strong: #1f3a68;
    --bullet: #3cb0ea;
    --footer-text: #1f3a68;
  }
  html, body {
    margin: 0;
    padding: 0;
    overflow: hidden;
  }
  .slide {
    position: relative;
    width: 1200px;
    height: 900px;
    overflow: hidden;
    background: var(--paper);
    font-family: "Carlito", "Calibri", sans-serif;
  }
  .slide-header {
    position: absolute;
    inset: 0 0 auto 0;
    height: 300px;
  }
  .slide-header svg {
    display: block;
  }
  .slide-title {
    position: absolute;
    top: 86px;
    left: 0;
    width: 100%;
    margin: 0;
    text-align: center;
    color: var(--paper);
    font-weight: 700;
    font-size: 74px;
    line-height: 94px;
  }
  .point-list {
    position: absolute;
    top: 356px;
    left: 128px;
    margin: 0;
    padding: 0;
    list-style: none;
  }
  .point-list li {
    position: relative;
    padding-left: 36px;
    font-size: 60px;
    line-height: 87px;
    color: var(--ink);
    white-space: nowrap;
  }
  .point-list li::before {
    content: "*";
    position: absolute;
    left: 0;
    top: 4px;
    color: var(--bullet);
    font-size: 58px;
  }
  .point-list strong {
    color: var(--ink-strong);
    font-style: italic;
    font-weight: 700;
  }
  .talk-illustration {
    position: absolute;
    left: 550px;
    top: 475px;
    width: 570px;
    height: 395px;
  }
  .talk-bubble {
    position: absolute;
    background:
      radial-gradient(circle at 30% 35%, rgba(240, 80, 70, 0.55), transparent 45%),
      radial-gradient(circle at 70% 60%, rgba(40, 170, 220, 0.6), transparent 50%),
      radial-gradient(circle at 45% 75%, rgba(250, 190, 40, 0.5), transparent 45%),
      linear-gradient(135deg, #7fc8e8, #e88a9a 55%, #8ccf7a);
    opacity: 0.85;
  }
  .talk-bubble--large {
    left: 0;
    top: 0;
    width: 460px;
    height: 360px;
    border-radius: 50% 50% 46% 48% / 52% 52% 46% 48%;
  }
  .talk-bubble--small {
    left: 400px;
    top: 135px;
    width: 170px;
    height: 260px;
    border-radius: 50% 50% 46% 46% / 40% 40% 58% 58%;
  }
  .brand {
    position: absolute;
    left: 20px;
    bottom: 24px;
    display: flex;
    align-items: center;
    gap: 10px;
  }
  .brand-dot {
    width: 18px;
    height: 18px;
    border-radius: 50%;
    background: var(--bullet);
  }
  .brand-name {
    font-size: 22px;
    font-weight: 400;
    color: var(--footer-text);
  }
</style>
</head>
<body>
<main class="slide">
  <header class="slide-header">
    <svg width="1200" height="300" viewBox="0 0 1200 300" aria-hidden="true">
      <defs>
        <linearGradient id="headerSky" x1="0" y1="0" x2="0" y2="1">
          <stop offset="0" stop-color="#1a8ad6"/>
          <stop offset="1" stop-color="#3aa6ea"/>
        </linearGradient>
      </defs>
      <path d="M0 0 H1200 V205 C980 215 820 245 640 232 C420 216 200 215 0 258 Z" fill="url(#headerSky)"/>
      <path d="M0 258 C200 215 420 216 640 232 C820 245 980 215 1200 205 V240 C1000 236 820 270 620 262 C400 252 200 248 0 282 Z" fill="#8fd0f6" opacity="0.7"/>
      <path d="M0 282 C200 248 400 252 620 262 C820 270 1000 236 1200 240 V300 H0 Z" fill="#ffffff"/>
      <path d="M560 300 C760 250 980 215 1200 218" fill="none" stroke="#d4eefc" stroke-width="2"/>
      <path d="M640 300 C840 262 1020 232 1200 232" fill="none" stroke="#d4eefc" stroke-width="2"/>
      <path d="M700 240 C860 262 1040 276 1200 262" fill="none" stroke="#8fd0f6" stroke-width="2" opacity="0.8"/>
    </svg>
    <h1 class="slide-title">Networking</h1>
  </header>

  <ul class="point-list">
    <li><strong>Invest time</strong> in your career</li>
    <li><strong>Make</strong> the time</li>
  </ul>

  <div class="talk-illustration" role="img" aria-label="Two speech bubbles filled with a colourful mosaic of small people and chat icons, representing networking">
    <div class="talk-bubble talk-bubble--large"></div>
    <div class="talk-bubble talk-bubble--small"></div>
  </div>

  <footer class="brand">
    <span class="brand-dot"></span>
    <span class="brand-name">Harbourline Coaching</span>
  </footer>
</main>
</body>
</html>
```